Cedar Harbor Business Cards For New Startup

I am looking for you to design some business cards for a new startup https://cedarharborhub.com. I have supplied logo, brand guidelines and our signatures as a guide.

We need this to reflect the brand guidelines and the website for brand consistency,

What is Cedar Harbor?

Mallorca's Business Growth Community
Join your new business community full of passionate entrepreneurs who
love to solve problems and help each other grow together!

Any questions you can ask.

Target Market(s)

Business to Business

Contact Information for Business Card

These are attached (signatures) to the job

Font styles to use
Other font styles liked:
• Open Sans

Requirements
Must have
• Match design guidelines
Nice to have
• Photos of our faces so people remember us

```html
<!DOCTYPE html>
<html lang="en">
<head>
<meta charset="utf-8">
<title>Cedar Harbor Business Cards</title>
<link rel="stylesheet" href="https://fonts.googleapis.com/css2?family=Open+Sans:wght@400;600;700&display=swap">
<style>
  :root {
    --olive: #6b6900;
    --olive-light: #777510;
    --white: #ffffff;
    --backdrop: #262626;
    --frame: #1a1a1a;
  }
  * { margin: 0; padding: 0; box-sizing: border-box; }
  html, body {
    width: 1125px;
    height: 1200px;
    overflow: hidden;
    background: var(--backdrop);
    font-family: "Open Sans", Arial, sans-serif;
  }
  .canvas { position: relative; width: 1125px; height: 1200px; }
  .card {
    position: absolute;
    left: 150px;
    width: 826px;
    height: 471px;
    border-radius: 20px;
    overflow: hidden;
    background: var(--olive);
    color: var(--white);
  }
  .card-front { top: 106px; }
  .card-back { top: 639px; }

  .front-emblem { position: absolute; inset: 0; width: 826px; height: 471px; }
  .emblem-name {
    font-family: "Open Sans", Arial, sans-serif;
    font-weight: 700;
    font-size: 40px;
    fill: var(--olive);
  }

  .portrait {
    position: absolute;
    left: 43px;
    top: 50px;
    width: 114px;
    height: 119px;
    border-radius: 10px;
    border: 1.5px solid var(--frame);
    background: linear-gradient(180deg, #e9e9e6 0%, #d8cfc4 45%, #4f6079 100%);
  }
  .identity { position: absolute; left: 43px; top: 192px; }
  .person-name {
    font-size: 30px;
    font-weight: 700;
    letter-spacing: 0.3px;
    line-height: 36px;
    text-transform: uppercase;
  }
  .person-role, .person-company {
    font-size: 20px;
    font-weight: 400;
    line-height: 27px;
  }
  .contact-list {
    position: absolute;
    left: 43px;
    top: 289px;
    list-style: none;
  }
  .contact-item {
    display: flex;
    align-items: center;
    height: 26px;
    font-size: 20px;
    line-height: 26px;
  }
  .contact-icon { width: 18px; height: 18px; margin-right: 13px; flex: none; }
  .social-row {
    position: absolute;
    left: 43px;
    top: 398px;
    display: flex;
    gap: 4px;
  }
  .social-square {
    width: 24px;
    height: 24px;
    background: var(--white);
    border-radius: 2px;
  }

  .back-pattern {
    position: absolute;
    inset: 0;
    background: radial-gradient(circle at 40% 40%, var(--olive-light) 0%, var(--olive) 75%);
  }
  .back-brand {
    position: absolute;
    left: 472px;
    width: 400px;
    top: 346px;
    text-align: center;
    font-size: 26px;
    font-weight: 700;
    line-height: 34px;
  }
  .back-url {
    position: absolute;
    left: 472px;
    width: 400px;
    top: 401px;
    text-align: center;
    font-size: 19px;
    font-weight: 400;
    line-height: 26px;
  }
</style>
</head>
<body>
<main class="canvas">

  <section class="card card-front" aria-label="Business card front">
    <svg class="front-emblem" viewBox="0 0 826 471" aria-hidden="false">
      <circle cx="603" cy="234" r="256" fill="none" stroke="#ffffff" stroke-width="2"/>
      <circle cx="603" cy="234" r="240" fill="#ffffff"/>
      <text class="emblem-name" x="640" y="248" text-anchor="middle">Cedar Harbor</text>
    </svg>

    <div class="portrait" role="img" aria-label="Portrait photo of Daniel Moreno"></div>

    <div class="identity">
      <h1 class="person-name">Daniel Moreno</h1>
      <p class="person-role">Founder &amp; Growth Hacker</p>
      <p class="person-company">Cedar Harbor</p>
    </div>

    <ul class="contact-list">
      <li class="contact-item">
        <svg class="contact-icon" viewBox="0 0 18 18" aria-hidden="true">
          <rect x="4" y="1" width="10" height="16" rx="1.5" fill="none" stroke="#fff" stroke-width="1.8"/>
          <rect x="7.5" y="13.5" width="3" height="1.4" fill="#fff"/>
        </svg>
        +34 600 482 715
      </li>
      <li class="contact-item">
        <svg class="contact-icon" viewBox="0 0 18 18" aria-hidden="true">
          <rect x="1" y="4" width="16" height="11" fill="#fff"/>
          <path d="M1 4 L9 10 L17 4" fill="none" stroke="#6b6900" stroke-width="1.4"/>
        </svg>
        dm@cedarharborhub.com
      </li>
      <li class="contact-item">
        <svg class="contact-icon" viewBox="0 0 18 18" aria-hidden="true">
          <circle cx="9" cy="9" r="8" fill="#fff"/>
          <ellipse cx="9" cy="9" rx="3.4" ry="8" fill="none" stroke="#6b6900" stroke-width="1.2"/>
          <line x1="1" y1="9" x2="17" y2="9" stroke="#6b6900" stroke-width="1.2"/>
        </svg>
        www.cedarharborhub.com
      </li>
    </ul>

    <div class="social-row" aria-label="Social profiles">
      <span class="social-square"></span>
      <span class="social-square"></span>
      <span class="social-square"></span>
      <span class="social-square"></span>
      <span class="social-square"></span>
    </div>
  </section>

  <section class="card card-back" aria-label="Business card back">
    <div class="back-pattern" role="img" aria-label="Repeating brand pattern in soft olive tones"></div>
    <p class="back-brand">Cedar Harbor</p>
    <p class="back-url">www.cedarharborhub.com</p>
  </section>

</main>
</body>
</html>
```